IT Network Consultancy - Business Card

t4 linkways is a IT network consultancy based in London. We're looking for a smart, modern and professional business card design. Our website is here: www.t4linkways.co.uk

Key things that should be included on the card (with examples):

Company Logo
Name
Position / Job Title: Network Consultant
Mobile Phone Number: +44 (0) 7700 900418
Land Line: +44 (0) 1632 960274
Email Address: name@t4linkways.co.uk
Web Site URL: www.t4linkways.co.uk

Target Market(s)

Large enterprise / global companies / corporates

Industry/Entity Type

Business

Requirements
Must have
• Incorporate our logo - which is attached to the project. They are in AI format (can be opened in Inkscape).

The design should be double sided and fit on a UK standard 85mm × 55mm card and be in a format that retains the quality when printed.
Nice to have
• The project does not have to conform to the colour of our website but this should give you inspiration of the style we like.
Should not have
• Bright colours. Pictures are not necessary.

```html
<!DOCTYPE html>
<html lang="en">
<head>
<meta charset="utf-8">
<title>t4 linkways – Business Card</title>
<link rel="stylesheet" href="https://fonts.googleapis.com/css2?family=Source+Sans+3:wght@400;600;700&display=swap">
<style>
  :root {
    --page: #ffffff;
    --card-front: #ffffff;
    --card-back: #8d9198;
    --ink: #1e1e1e;
    --ink-soft: #8a8d92;
    --brand: #6b6f76;
    --brand-light: #ffffff;
    --watermark: #ececec;
    --card-edge: #e4e4e4;
  }
  * { margin: 0; padding: 0; box-sizing: border-box; }
  html, body {
    width: 1200px;
    height: 900px;
    overflow: hidden;
    background: var(--page);
    font-family: "Source Sans 3", "Helvetica Neue", Arial, sans-serif;
  }
  .canvas { position: relative; width: 1200px; height: 900px; }

  .card { position: absolute; width: 589px; height: 380px; overflow: hidden; }

  /* Back side */
  .card--back {
    left: 521px; top: 394px;
    background: var(--card-back);
    z-index: 1;
  }
  .card__pattern {
    position: absolute; inset: 0;
    background: var(--card-back);
  }
  .card__brand--back {
    position: absolute;
    left: 0; right: 0; top: 182px;
    text-align: center;
    color: var(--brand-light);
    font-size: 40px;
    font-weight: 600;
    letter-spacing: 0.5px;
    line-height: 1;
  }

  /* Front side */
  .card--front {
    left: 78px; top: 113px;
    background: var(--card-front);
    border: 1px solid var(--card-edge);
    z-index: 2;
  }
  .card__watermark {
    position: absolute;
    left: -10px; top: 190px;
    width: 200px; height: 200px;
    border-radius: 50%;
    background: var(--watermark);
  }
  .person { position: absolute; left: 267px; top: 70px; }
  .person__name { font-size: 18px; font-weight: 700; color: var(--ink); line-height: 22px; }
  .person__role { font-size: 15px; font-weight: 400; color: var(--ink-soft); line-height: 20px; }

  .card__brand--front {
    position: absolute;
    left: 189px; top: 220px;
    display: flex; align-items: center; gap: 10px;
    color: var(--brand);
    font-size: 34px;
    font-weight: 400;
    line-height: 1;
  }
  .brand-dot {
    width: 30px; height: 30px;
    border-radius: 50%;
    background: var(--brand);
  }

  .contact {
    position: absolute;
    left: 267px; top: 265px;
    display: grid;
    grid-template-columns: 90px auto;
    row-gap: 0;
    font-size: 15.5px;
    line-height: 19.5px;
  }
  .contact__label { font-weight: 700; color: var(--ink); }
  .contact__value { font-weight: 400; color: #4a4c50; }
</style>
</head>
<body>
<main class="canvas">

  <section class="card card--back" aria-label="Card back">
    <div class="card__pattern" role="img" aria-label="Repeating outlined brand-mark pattern in light grey lines"></div>
    <p class="card__brand--back">t4 linkways</p>
  </section>

  <section class="card card--front" aria-label="Card front">
    <div class="card__watermark" role="img" aria-label="Large faint brand decoration"></div>

    <div class="person">
      <p class="person__name">Daniel Marsh</p>
      <p class="person__role">Network Consultant</p>
    </div>

    <div class="card__brand--front">
      <span class="brand-dot"></span>
      <span>t4 linkways</span>
    </div>

    <dl class="contact">
      <dt class="contact__label">Mobile</dt>
      <dd class="contact__value">+44 (0) 7700 900418</dd>
      <dt class="contact__label">Land Line</dt>
      <dd class="contact__value">+44 (0) 1632 960274</dd>
      <dt class="contact__label">Email</dt>
      <dd class="contact__value">name@t4linkways.co.uk</dd>
      <dt class="contact__label">Web</dt>
      <dd class="contact__value">www.t4linkways.co.uk</dd>
    </dl>
  </section>

</main>
</body>
</html>
```